Tallowreed Advisory Partners Business Card Design

We have the logo we just need someone to design a modern business card design.

Name: Desmond Munkalt
Phone: 3055550148
Mobile: 9175550193
Web:www.tallowreedadvisory.example
email: dmunkalt@tallowreedadvisory.example
Company: Tallowreed Advisory Partners
Title: CEO

Address: 718 Quillmore Ave, Miami, Florida 33190

Target Market(s)

companies over 100 employees

Industry/Entity Type

Business

```html
<!DOCTYPE html>
<html lang="en">
<head>
<meta charset="UTF-8">
<title>Tallowreed Advisory Partners – Business Card</title>
<link rel="stylesheet" href="https://fonts.googleapis.com/css2?family=Open+Sans:wght@400;600&display=swap">
<style>
  :root {
    --canvas-bg: #e9ebee;
    --brand-blue: #1b7bd3;
    --brand-blue-light: #3a8fdc;
    --brand-navy: #123a66;
    --card-white: #ffffff;
    --text-dark: #2b2f36;
    --divider: #d4d7db;
  }
  * { box-sizing: border-box; margin: 0; padding: 0; }
  html, body {
    width: 1200px;
    height: 900px;
    overflow: hidden;
    background: var(--canvas-bg);
    font-family: "Open Sans", Arial, sans-serif;
  }
  .canvas {
    position: relative;
    width: 1200px;
    height: 900px;
  }
  .card {
    position: absolute;
    width: 700px;
    height: 400px;
    overflow: hidden;
    box-shadow: 0 10px 30px rgba(0, 0, 0, 0.18);
  }

  /* Back of card */
  .card-back {
    left: 140px;
    top: 40px;
    background: var(--brand-blue);
  }
  .card-back .backdrop-circle {
    position: absolute;
    left: -40px;
    top: 110px;
    width: 360px;
    height: 360px;
    border-radius: 50%;
    background: var(--brand-blue-light);
    opacity: 0.55;
  }
  .card-back .brand {
    position: absolute;
    left: 390px;
    top: 120px;
    color: var(--card-white);
  }

  /* Shared brand lockup */
  .brand {
    display: flex;
    flex-direction: column;
    align-items: center;
    gap: 12px;
    font-weight: 600;
    text-align: center;
  }
  .brand-dot {
    width: 46px;
    height: 46px;
    border-radius: 50%;
    background: currentColor;
  }
  .brand-name {
    font-size: 30px;
    line-height: 1.05;
    letter-spacing: -0.5px;
  }
  .brand-name small {
    display: block;
    font-size: 17px;
    letter-spacing: 0.5px;
    margin-top: 4px;
  }

  /* Front of card */
  .card-front {
    left: 360px;
    top: 470px;
    background: var(--card-white);
  }
  .card-front .brand {
    position: absolute;
    left: 20px;
    top: 110px;
    width: 220px;
    color: var(--brand-navy);
  }
  .card-front .brand-dot { background: var(--brand-blue); }
  .card-front .divider {
    position: absolute;
    left: 262px;
    top: 40px;
    width: 2px;
    height: 300px;
    background: var(--divider);
  }
  .contact {
    position: absolute;
    right: 34px;
    top: 48px;
    width: 400px;
    text-align: right;
  }
  .contact-name {
    color: var(--brand-blue);
    font-size: 32px;
    font-weight: 600;
    letter-spacing: 0.3px;
    margin-bottom: 42px;
  }
  .contact-lines {
    list-style: none;
    font-size: 14.5px;
    line-height: 1.6;
    letter-spacing: 0.4px;
    color: var(--text-dark);
    font-weight: 600;
  }
  .contact-lines .accent { color: var(--brand-blue); }
  .card-front .base-band {
    position: absolute;
    left: 0;
    bottom: 0;
    width: 100%;
    height: 26px;
    background: var(--brand-blue);
  }
</style>
</head>
<body>
<main class="canvas">

  <section class="card card-back" aria-label="Card back">
    <div class="backdrop-circle"></div>
    <div class="brand">
      <span class="brand-dot"></span>
      <span class="brand-name">Tallowreed<small>advisory partners</small></span>
    </div>
  </section>

  <section class="card card-front" aria-label="Card front">
    <div class="brand">
      <span class="brand-dot"></span>
      <span class="brand-name">Tallowreed<small>advisory partners</small></span>
    </div>
    <div class="divider"></div>
    <div class="contact">
      <h1 class="contact-name">Desmond Munkalt</h1>
      <ul class="contact-lines">
        <li class="accent">Phone: 3055550148</li>
        <li class="accent">Mobile: 9175550193</li>
        <li>Web:www.tallowreedadvisory.example</li>
        <li>email: dmunkalt@tallowreedadvisory.example</li>
        <li>Company: Tallowreed Advisory Partners</li>
        <li>Title: CEO</li>
      </ul>
    </div>
    <div class="base-band"></div>
  </section>

</main>
</body>
</html>
```